Business Card for Luxury Hospitality Industry Career Seeker

Need something Simple, Punctual, and Elegant.

Project goal is to update phone number, layout, and wording

I look forward to working with you to create a business card I can give to managers and employers in the Luxury Hospitality industry. I want to advance a career in this industry handing out cards to managers and directors on my way up.
Updates

Updated graphics preferences in brief - would like my name flanked by small Lion, Compass, & Rope and have the Halworth 5 Star logo on the back Added Saturday, January 14, 2017

Updated Brief:-Some wording has been removed-Card Front should be more simple and tidy now-Card Back word choice & flow is improved Added Sunday, January 15, 2017

Target Market(s)

Luxury Hospitality Industry Employers and Managers

Industry/Entity Type

Hospitality

Contact Information for Business Card

(Card Front)
Corbin T. Pellman (flanked by small Lion, Compass & Rope graphic)
Luxury Hospitality
555-317-8846
ridgefellow@mailvessel.example
netroster.example/in/corbin-pellman-vet-civ
My Experience = Our Success

(Card Back)
Graphic of: Halworth 5 Star logo and maybe QTR 5 Diamond Logo too
8 years military supply, logistics, & administrative experience
2 years intensive recruiting, marketing, and sales expertise
Adept problem solving, planning and management skills
5 Star, 5 Daimond, Luxury Hotels & Hospitality Rooms & Revenue

Requirements
Must have
• Name
• Phone Number
• Email Address
• Net Roster Address
• Slogan (My Experience = Our Success)
• Graphic on back: Halworth 5 Star logo
• Qualification Remarks
• Catchy logo
Nice to have
• Background that makes a viewer think Luxury Hospitality Experience and/or World Experience
• Color combinations I've seen & liked are black & yellow, black & white, and blue & white

```html
<!DOCTYPE html>
<html lang="en">
<head>
<meta charset="utf-8">
<title>Corbin T. Pellman – Business Card</title>
<link href="https://fonts.googleapis.com/css2?family=Montserrat:wght@400;500&family=Raleway:wght@300&display=swap" rel="stylesheet">
<style>
  :root {
    --canvas: #ececec;
    --card-black: #0b0b0b;
    --card-charcoal: #2a2a2a;
    --accent-yellow: #ece443;
    --ink-dark: #1e1c1c;
    --ink-light: #e6e6e6;
    --paper: #ffffff;
    --emblem: #d9d9d9;
  }
  * { margin: 0; padding: 0; box-sizing: border-box; }
  html, body {
    width: 1200px; height: 731px; overflow: hidden;
    background: var(--canvas);
    font-family: "Montserrat", sans-serif;
  }
  .stage { position: relative; width: 1200px; height: 731px; }
  .card {
    position: absolute; top: 244px;
    width: 327px; height: 182px; overflow: hidden;
  }
  .card-front {
    left: 262px;
    background: radial-gradient(ellipse at 50% 35%, var(--card-charcoal) 0%, var(--card-black) 75%);
    color: var(--ink-light); text-align: center;
  }
  .card-back { left: 614px; background: var(--paper); }

  .name-block { position: absolute; top: 42px; left: 0; width: 100%; }
  .name {
    font-family: "Raleway", sans-serif; font-weight: 300;
    color: var(--accent-yellow); font-size: 28px; line-height: 27px;
    letter-spacing: 0.5px; text-transform: uppercase;
  }
  .emblem {
    position: absolute; top: 18px; width: 16px; height: 16px;
    border-radius: 50%; background: var(--emblem);
  }
  .emblem-left { left: 76px; }
  .emblem-right { right: 17px; left: auto; }
  .emblem-right { left: 234px; }

  .rule { position: absolute; left: 92px; width: 143px; height: 1px; background: var(--ink-light); }
  .rule-top { top: 98px; }
  .rule-bottom { top: 114px; }
  .title { position: absolute; top: 102px; width: 100%; font-size: 8px; }
  .slogan { position: absolute; top: 118px; width: 100%; font-size: 8px; }
  .contact { position: absolute; top: 148px; width: 100%; font-size: 8px; line-height: 10px; }
  .link-band {
    position: absolute; bottom: 0; left: 0; width: 100%; height: 11px;
    background: var(--accent-yellow); color: var(--ink-dark);
    font-size: 8px; line-height: 11px; font-weight: 500;
  }

  .back-top {
    position: absolute; top: 0; left: 0; width: 100%; height: 108px;
    background: var(--accent-yellow);
  }
  .partner-mark {
    position: absolute; top: 60px; right: 14px;
    display: flex; align-items: center; gap: 4px;
    font-size: 10px; font-weight: 500; color: var(--ink-dark);
  }
  .partner-dot { width: 8px; height: 8px; border-radius: 50%; background: var(--ink-dark); }
  .back-slogan {
    position: absolute; top: 92px; right: 11px;
    font-size: 8px; color: var(--ink-dark);
  }
  .qualifications {
    position: absolute; top: 110px; left: 13px; list-style: none;
    font-size: 7.6px; line-height: 14.2px; color: var(--ink-dark);
  }
  .qualifications li { position: relative; padding-left: 8px; }
  .qualifications li::before {
    content: ""; position: absolute; left: 0; top: 5.5px;
    width: 3.5px; height: 3.5px; border-radius: 50%; background: var(--ink-dark);
  }
  .back-band {
    position: absolute; bottom: 0; left: 0; width: 100%; height: 11px;
    background: var(--ink-dark);
  }
</style>
</head>
<body>
<main class="stage">
  <section class="card card-front">
    <div class="name-block">
      <div class="emblem emblem-left" role="img" aria-label="Lion, Compass & Rope emblem"></div>
      <h1 class="name">Corbin T.<br>Pellman</h1>
      <div class="emblem emblem-right" role="img" aria-label="Lion, Compass & Rope emblem"></div>
    </div>
    <div class="rule rule-top"></div>
    <p class="title">Reservations Agent Halworth 5 Star Luxury Hotel</p>
    <div class="rule rule-bottom"></div>
    <p class="slogan">My Experience = Our Success</p>
    <p class="contact">ridgefellow@mailvessel.example<br>555-317-8846</p>
    <p class="link-band">netroster.example/in/corbin-pellman-vet-civ</p>
  </section>

  <section class="card card-back">
    <div class="back-top">
      <div class="partner-mark"><span class="partner-dot"></span>Halworth</div>
      <p class="back-slogan">My Experience = Our Success</p>
    </div>
    <ul class="qualifications">
      <li>8 Years military supply, logistics, &amp; administrative experience</li>
      <li>2 Years intensive recruiting, marketing, and sales expertise</li>
      <li>Adept problem solving, planning and management skills</li>
      <li>5 Star, 5 Daimond, Luxury Hotels &amp; Hospitality Rooms &amp; Revenue</li>
    </ul>
    <div class="back-band"></div>
  </section>
</main>
</body>
</html>
```